Presentation folder for holding wedding cake literature

We need to have a front cover design as well as a back cover design for a presentation folder to hold literature for a bakery who sells a lot of wedding cakes.

We have uploaded a couple copies of ideas that we like. They are for demonstrative purposes only.

The text on the front cover needs to be:
-The Sugar Atelier-
-Designing, baking and decorating perfect wedding cakes...Guaranteed!

On the back cover it needs to say:
-Serving VELVAsoft cakes and a "Silver Ribbon" Experience-

In addition the back cover must contain the "Silver Ribbon Baker" logo.

We will only supply photos if necessary. We would rather have you choose them.

We are open to any colors as long as they are soft.

For a reference of the client, go to http://www.brindlefieldsugaratelier.example

Target Market(s)

The target market is primarily women ages 25-40.

Industry/Entity Type

Wedding

Requirements
Must have
• Must have priorities are listed in the brief.
Nice to have
• Fonts should be a combination of "script" and one or more complementary styles.

Colors should be either a soft blue, pinkish tone or lavender tone. Mixing any of the colors with a light gray would be acceptable as well.
Should not have
• No dark colors such as black, red, purple, green or orange.

```html
<!DOCTYPE html>
<html lang="en">
<head>
<meta charset="utf-8">
<title>The Sugar Atelier – Presentation Folder</title>
<link href="https://fonts.googleapis.com/css2?family=Dosis:wght@500;600&family=Open+Sans:wght@400;600&display=swap" rel="stylesheet">
<style>
  :root {
    --bg: #ededed;
    --paper: #ffffff;
    --gold: #b8862b;
    --gold-pocket: #bf8f30;
    --green: #3aae4a;
    --ink: #333333;
    --logo-blue: #1d8fd0;
    --label: #555555;
  }
  * { box-sizing: border-box; margin: 0; padding: 0; }
  html, body { width: 1200px; height: 1032px; overflow: hidden; }
  body {
    background: var(--bg);
    font-family: "Open Sans", Arial, sans-serif;
    color: var(--ink);
    position: relative;
  }
  .panel {
    position: absolute;
    background: var(--paper);
    box-shadow: 0 4px 14px rgba(0,0,0,.12);
  }
  .back-cover { left: 170px; top: 70px; width: 380px; height: 500px; }
  .front-cover { left: 550px; top: 70px; width: 380px; height: 500px; overflow: hidden; }

  .back-cover .tagline {
    position: absolute; top: 100px; left: 0; width: 100%;
    text-align: center; font-size: 12px; line-height: 1.35;
  }
  .tagline .highlight {
    display: block; color: var(--gold); font-size: 22px; line-height: 1.1;
  }
  .brand-mark {
    position: absolute; top: 250px; left: 0; width: 100%;
    display: flex; justify-content: center; align-items: center; gap: 8px;
    font-size: 20px; font-weight: 600; color: var(--logo-blue);
  }
  .brand-mark .dot { width: 14px; height: 14px; border-radius: 50%; background: var(--logo-blue); }
  .contact {
    position: absolute; bottom: 40px; left: 40px; right: 30px;
    font-size: 7.5px; line-height: 1.6; color: var(--ink);
  }
  .contact svg { vertical-align: -1px; margin-right: 3px; }

  .front-cover .art { position: absolute; inset: 0; }
  .front-cover .title-block {
    position: absolute; top: 28px; right: 34px; text-align: right;
  }
  .title-block .name {
    font-family: "Dosis", sans-serif; font-weight: 600;
    color: var(--gold); font-size: 22px; letter-spacing: .3px;
  }
  .title-block .line1 { font-size: 11px; margin-top: 8px; }
  .title-block .line2 { font-size: 14px; }
  .title-block .promise {
    font-family: "Dosis", sans-serif; font-weight: 600;
    color: var(--gold); font-size: 18px; margin-top: 4px;
  }

  .label { position: absolute; font-size: 21px; color: var(--label); }
  .label-back { left: 352px; top: 645px; }
  .label-front { left: 826px; top: 582px; }
  .label-inside { left: 975px; top: 977px; font-size: 22px; }

  .inside-leaf { position: absolute; top: 716px; width: 470px; height: 290px; background: var(--paper); box-shadow: 0 4px 14px rgba(0,0,0,.1); }
  .inside-left { left: 130px; }
  .inside-right { left: 620px; background: #f4f4f4; }
  .pocket { position: absolute; left: 0; right: 0; bottom: 0; height: 120px; background: var(--gold-pocket); }
</style>
</head>
<body>

  <section class="panel back-cover" aria-label="Back cover">
    <p class="tagline">Serving VELVAsoft cakes and a
      <span class="highlight">"Silver Ribbon"</span>Experience</p>
    <div class="brand-mark"><span class="dot"></span>Silver Ribbon Baker</div>
    <div class="contact">
      <div><svg width="7" height="8" viewBox="0 0 7 8"><path d="M3.5 0a3 3 0 0 1 3 3c0 2-3 5-3 5S.5 5 .5 3a3 3 0 0 1 3-3z" fill="#333"/></svg>000 Harbor Lane Suite 000 Fairview, CA 90000</div>
      <div><svg width="7" height="7" viewBox="0 0 7 7"><rect x="1" y="0" width="5" height="7" rx="1" fill="#333"/></svg>000 000 0000 &nbsp;
        <svg width="7" height="7" viewBox="0 0 7 7"><rect x="0" y="1" width="7" height="5" fill="#333"/></svg>000 000 0000 &nbsp;
        <svg width="8" height="6" viewBox="0 0 8 6"><rect width="8" height="6" fill="#333"/></svg>info@sugaratelier.example</div>
    </div>
  </section>

  <section class="panel front-cover" aria-label="Front cover">
    <svg class="art" width="380" height="500" viewBox="0 0 380 500">
      <defs>
        <linearGradient id="photoTone" x1="0" y1="0" x2="0" y2="1">
          <stop offset="0" stop-color="#9c8a9a"/>
          <stop offset=".5" stop-color="#4a3f3c"/>
          <stop offset="1" stop-color="#8fd3e0"/>
        </linearGradient>
        <linearGradient id="cakeTone" x1="0" y1="0" x2="1" y2="0">
          <stop offset="0" stop-color="#f3f3f3"/>
          <stop offset=".5" stop-color="#ebebeb"/>
          <stop offset="1" stop-color="#f7f7f7"/>
        </linearGradient>
      </defs>
      <rect x="230" y="70" width="150" height="430" fill="url(#cakeTone)" role="img" aria-label="Faded tall white tiered wedding cake"/>
      <path d="M0 0 H14 Q150 210 250 500 H0 Z" fill="url(#photoTone)" role="img" aria-label="Collage of wedding photos: balloons, champagne toast, couple cutting a blue tiered cake"/>
      <path d="M14 0 Q150 210 250 500 H264 Q170 220 20 0 Z" fill="var(--green)"/>
    </svg>
    <div class="title-block">
      <div class="name">The Sugar Atelier</div>
      <div class="line1">Designing, baking and decorating</div>
      <div class="line2">perfect wedding cakes...</div>
      <div class="promise">Guaranteed!</div>
    </div>
  </section>

  <span class="label label-back">Back Side</span>
  <span class="label label-front">Front Side</span>

  <section class="inside-leaf inside-left" aria-label="Inside left leaf"><div class="pocket"></div></section>
  <section class="inside-leaf inside-right" aria-label="Inside right leaf"><div class="pocket"></div></section>

  <span class="label label-inside">Inside Leaf</span>

</body>
</html>
```